Business Card *

A business card design
Use the logo uploaded in the brief page.
You may use placeholders in your design layouts.
I will provide the actual business card details to the winning designer.

Logo
Place for contact info (name, title, phone, email, etc)

Requirements
Must have
• Logo

```html
<!DOCTYPE html>
<html lang="en">
<head>
<meta charset="utf-8">
<title>Harrowfield Business Card</title>
<link rel="stylesheet" href="https://fonts.googleapis.com/css2?family=Arimo:wght@400;700&display=swap">
<style>
  :root {
    --backdrop: #2b2b2b;
    --card: #f7f7f7;
    --ink-grey: #6a6a6a;
    --ink-soft: #7a7a7a;
    --brand-green: #3aa935;
    --rule-grey: #9a9a9a;
    --corner-grey: #8c8c8c;
  }
  * { box-sizing: border-box; margin: 0; padding: 0; }
  html, body {
    width: 1200px; height: 997px; overflow: hidden;
    background: var(--backdrop);
    font-family: "Arimo", Arial, sans-serif;
  }
  .stage { position: relative; width: 1200px; height: 997px; }

  .card {
    position: absolute;
    background: var(--card);
    box-shadow: 0 14px 40px rgba(0,0,0,.55);
    overflow: hidden;
  }

  /* Back of card (landscape) */
  .card-back {
    left: 90px; top: 300px; width: 540px; height: 310px;
    display: flex; align-items: center; justify-content: center;
  }
  .brand { display: flex; align-items: center; gap: 12px; }
  .brand-dot {
    width: 34px; height: 34px; border-radius: 50%;
    background: var(--brand-green);
  }
  .brand-name {
    font-weight: 700; color: var(--ink-grey);
    letter-spacing: 1px;
  }
  .card-back .brand-name { font-size: 40px; }

  /* Front of card (portrait) */
  .card-front {
    left: 690px; top: 150px; width: 390px; height: 680px;
    padding: 80px 44px 0 44px;
  }
  .card-front .brand { justify-content: center; }
  .card-front .brand-name { font-size: 36px; }

  .person { margin-top: 250px; }
  .person-name {
    font-weight: 700; font-size: 22px; color: var(--ink-grey);
    letter-spacing: .5px;
  }
  .person-title { font-size: 18px; color: var(--brand-green); margin-top: 2px; }
  .rule { height: 1px; width: 62px; margin: 16px 0 22px; background: var(--rule-grey); }
  .rule.green { height: 2px; background: var(--brand-green); margin: 10px 0 14px; }

  .address { font-size: 15px; line-height: 1.3; color: var(--ink-soft); }

  .contact-list { list-style: none; }
  .contact-list li {
    display: flex; align-items: center; gap: 10px;
    font-size: 16px; color: var(--ink-soft); margin-bottom: 8px;
  }
  .contact-icon {
    width: 22px; height: 22px; border-radius: 50%;
    background: var(--brand-green);
    display: flex; align-items: center; justify-content: center;
    flex: none;
  }
  .website {
    font-weight: 700; font-size: 17px; color: var(--brand-green);
    margin-top: 6px;
  }

  .band {
    position: absolute; left: 0; bottom: 0; width: 100%; height: 34px;
  }
</style>
</head>
<body>
<main class="stage">

  <section class="card card-back" aria-label="Business card back">
    <div class="brand">
      <span class="brand-dot"></span>
      <span class="brand-name">HARROWFIELD</span>
    </div>
  </section>

  <section class="card card-front" aria-label="Business card front">
    <div class="brand">
      <span class="brand-dot"></span>
      <span class="brand-name">HARROWFIELD</span>
    </div>

    <div class="person">
      <p class="person-name">NORA PELL</p>
      <p class="person-title">Director</p>
    </div>
    <div class="rule"></div>

    <p class="address">Unit 8, Mill Lane,<br>Pune, India.</p>
    <div class="rule green"></div>

    <ul class="contact-list">
      <li>
        <span class="contact-icon">
          <svg width="12" height="12" viewBox="0 0 24 24" aria-hidden="true">
            <path fill="#fff" d="M6.6 10.8a15 15 0 0 0 6.6 6.6l2.2-2.2c.3-.3.7-.4 1-.2 1.1.4 2.3.6 3.6.6.6 0 1 .4 1 1V20c0 .6-.4 1-1 1A17 17 0 0 1 3 4c0-.6.4-1 1-1h3.5c.6 0 1 .4 1 1 0 1.3.2 2.5.6 3.6.1.3 0 .7-.2 1z"/>
          </svg>
        </span>
        0400 555 017
      </li>
      <li>
        <span class="contact-icon">
          <svg width="12" height="12" viewBox="0 0 24 24" aria-hidden="true">
            <rect x="3" y="6" width="18" height="12" fill="none" stroke="#fff" stroke-width="2"/>
            <path d="M3 6l9 7 9-7" fill="none" stroke="#fff" stroke-width="2"/>
          </svg>
        </span>
        norapell@harrowfield.com
      </li>
    </ul>
    <p class="website">www.harrowfield.com</p>

    <svg class="band" viewBox="0 0 390 34" preserveAspectRatio="none" aria-hidden="true">
      <polygon points="0,34 0,30 390,18 390,34" fill="var(--brand-green)"/>
      <polygon points="0,34 0,20 170,25 190,34" fill="var(--corner-grey)"/>
    </svg>
  </section>

</main>
</body>
</html>
```